Managed Service Provider need new business cards

We are a small Maanged Service Provider of IT Services and need a new fresh design for our business cards. We want something impossible, fun and professional :)
Our services has a large range, but we are always fun and make sure our customers both get their issue sorted and also feel like they are "catching up with an old friend".
All our cards in the past has always been all black, with red and we need something fresher.
The back of card, we would like just a small list of what we do i think, but if someone has a better idea, please do something cool with the back of the card:
Managed IT Services
Productivity Solutions
Data Backup and Recovery
IT System Maintenance
Managed IT Security
More details can be found on our website tqnetworks.com.au
Industry/Entity Type
It Company
Contact Information for Business Card
Name: Dwayne Falstrup
Title: Director
Phone: 03 6193 4827
Mobile: 0412 587 239
Email: dwayne@tqnetworks.com.au
Web: www.tqnetworks.com.au

```html
<!DOCTYPE html>
<html lang="en">
<head>
<meta charset="utf-8">
<title>TQ Networks – Business Cards</title>
<link rel="stylesheet" href="https://fonts.googleapis.com/css2?family=Bebas+Neue&family=Arimo:wght@400&display=swap">
<style>
  :root {
    --brand-red: #ed1c24;
    --card-white: #ffffff;
    --ink: #1a1a1a;
    --rule: #9a9a9a;
    --backdrop: #a3a3a3;
  }
  * { margin: 0; padding: 0; box-sizing: border-box; }
  html, body { width: 1200px; height: 1200px; overflow: hidden; }
  body {
    background: var(--backdrop);
    position: relative;
    font-family: "Arimo", Arial, sans-serif;
  }
  .card {
    position: absolute;
    top: 303px;
    width: 370px;
    height: 594px;
  }
  .card--back { left: 200px; background: var(--brand-red); color: var(--card-white); }
  .card--front { left: 598px; width: 366px; background: var(--card-white); color: var(--ink); }

  .wordmark {
    position: absolute;
    left: 0; right: 0;
    text-align: center;
    font-family: "Bebas Neue", "Oswald", sans-serif;
    font-weight: 400;
    line-height: 1;
    letter-spacing: 1px;
  }
  .card--back .wordmark { top: 500px; top: 197px; font-size: 72px; color: var(--card-white); }
  .card--front .wordmark { top: 130px; font-size: 68px; color: var(--brand-red); }

  .services {
    position: absolute;
    top: 422px;
    left: 0; right: 0;
    list-style: none;
    text-align: center;
    font-size: 18px;
    line-height: 26.8px;
    letter-spacing: 0.2px;
    text-transform: uppercase;
  }

  .holder {
    position: absolute;
    top: 372px;
    left: 0; right: 0;
    text-align: center;
  }
  .holder__name {
    font-family: "Bebas Neue", "Oswald", sans-serif;
    font-size: 29px;
    line-height: 1;
    color: var(--brand-red);
    letter-spacing: 0.3px;
  }
  .holder__title { font-size: 17px; line-height: 20px; margin-top: 0; }

  .icon-row {
    position: absolute;
    top: 434px;
    left: 0; right: 0;
    display: flex;
    justify-content: center;
    align-items: center;
    gap: 4px;
  }
  .icon-row__rule { width: 35px; height: 1px; background: var(--rule); margin: 0 4px; }
  .icon {
    width: 25px; height: 25px;
    border-radius: 4px;
    background: var(--brand-red);
    display: flex; align-items: center; justify-content: center;
  }
  .icon svg { width: 17px; height: 17px; }

  .contacts {
    position: absolute;
    top: 470px;
    left: 0; right: 0;
    text-align: center;
    font-size: 17px;
    line-height: 21.4px;
  }
  .contacts .accent { color: var(--brand-red); }
</style>
</head>
<body>

  <section class="card card--back">
    <div class="wordmark">TQ NETWORKS</div>
    <ul class="services">
      <li>Managed IT Services</li>
      <li>Productivity Solutions</li>
      <li>Data Backup and Recovery</li>
      <li>IT System Maintenance</li>
      <li>Managed IT Security</li>
    </ul>
  </section>

  <section class="card card--front">
    <div class="wordmark">TQ NETWORKS</div>

    <div class="holder">
      <div class="holder__name">DWAYNE FALSTRUP</div>
      <div class="holder__title">Director</div>
    </div>

    <div class="icon-row">
      <span class="icon-row__rule"></span>
      <span class="icon" aria-label="Phone">
        <svg viewBox="0 0 20 20" fill="none" stroke="#fff" stroke-width="1.6" stroke-linejoin="round">
          <path d="M3 8c0-2 3-3.5 7-3.5S17 6 17 8l-3 .5-.5-2h-7L6 8.5z" fill="#fff"/>
          <rect x="4.5" y="9.5" width="11" height="6" rx="1" fill="#fff"/>
        </svg>
      </span>
      <span class="icon" aria-label="Mobile">
        <svg viewBox="0 0 20 20" fill="none" stroke="#fff" stroke-width="1.6">
          <rect x="6" y="2.5" width="8" height="15" rx="1.5"/>
          <circle cx="10" cy="14.8" r="0.8" fill="#fff"/>
        </svg>
      </span>
      <span class="icon" aria-label="Email">
        <svg viewBox="0 0 20 20" fill="none" stroke="#fff" stroke-width="1.4">
          <rect x="2.5" y="5" width="15" height="10"/>
          <path d="M2.5 5l7.5 6 7.5-6M2.5 15l5.5-5M17.5 15l-5.5-5"/>
        </svg>
      </span>
      <span class="icon" aria-label="Website">
        <svg viewBox="0 0 20 20" fill="none" stroke="#fff" stroke-width="1.5">
          <circle cx="10" cy="10" r="7"/>
          <path d="M3 10h14M10 3c-2.5 2.5-2.5 11.5 0 14M10 3c2.5 2.5 2.5 11.5 0 14"/>
        </svg>
      </span>
      <span class="icon-row__rule"></span>
    </div>

    <div class="contacts">
      <div>03 6193 4827</div>
      <div>0412 587 239</div>
      <div>dwayne@tqnetworks.com.au</div>
      <div>www.<span class="accent">tqnetworks</span>.com.au</div>
    </div>
  </section>

</body>
</html>
```